Bread Baking Blog

I need theme modification/customization and logo for a Wordpress theme that I can use the blog about bread baking. Needs to include pictures & recipes.

Can provide access to my quillpage.com site. Have paid for https://plankvault.com/themes/brisk/ but open to alternatives.

The site name is "crumb42.com" (type 85 flour is a type of bread flour used in artisan bread baking). Not particular on color palette - am looking for your creativity.

I've included some logos for other domains I have to help provide some inspiration.

```html
<!DOCTYPE html>
<html lang="en">
<head>
<meta charset="utf-8">
<title>crumb42.com – Bread Baking Blog</title>
<link href="https://fonts.googleapis.com/css2?family=Montserrat:wght@600;700;800&family=Roboto:wght@400;500;700&display=swap" rel="stylesheet">
<style>
:root{
  --stage:#0d0d0d;
  --ink:#1e1e1e;
  --muted:#6b6b6b;
  --orange:#f7941d;
  --orange-dark:#e07c0a;
  --paper:#ffffff;
  --soft:#f2f2f2;
  --footer:#151515;
  --bar:#000000;
}
*{box-sizing:border-box;margin:0;padding:0}
html,body{width:1200px;height:2456px;overflow:hidden;background:var(--stage)}
body{font-family:Roboto,Arial,sans-serif;color:var(--ink);position:relative}
.page{position:absolute;left:248px;top:40px;width:704px;height:2390px;background:var(--paper)}
.brand{display:flex;align-items:center;gap:6px;font-family:Montserrat,Arial,sans-serif;font-weight:800;color:var(--orange);font-size:14px;letter-spacing:.5px;white-space:nowrap}
.brand .dot{width:14px;height:14px;border-radius:50%;background:var(--orange)}
/* hero */
.hero{position:relative;height:408px;background:radial-gradient(ellipse at 70% 85%,#6b4a25 0%,#2e2216 40%,#120d09 75%),#120d09}
.nav{position:absolute;top:26px;left:0;right:0;display:flex;align-items:center;justify-content:center;gap:22px;font-size:10px;color:#e8e8e8;white-space:nowrap}
.nav .active{color:var(--orange)}
.nav .brand{margin:0 10px}
.nav .search{width:12px;height:12px}
.nav .cta{background:var(--orange);color:#fff;padding:5px 14px;border-radius:12px;font-weight:500}
.hero h1{position:absolute;left:88px;top:136px;width:360px;font-family:Montserrat,Arial,sans-serif;font-weight:800;font-size:21px;line-height:24px;color:#fff;text-transform:uppercase;white-space:nowrap}
.hero p{position:absolute;left:88px;top:192px;width:260px;font-size:10px;line-height:14px;color:#ddd}
.hero .btn{position:absolute;left:88px;top:236px;background:var(--orange);color:#fff;font-size:10px;font-weight:500;padding:7px 18px;border-radius:14px}
/* categories */
.cats{position:absolute;top:432px;left:32px;right:32px;display:flex;gap:14px}
.cat{flex:1}
.cat .ph{height:86px}
.cat p{font-size:9px;line-height:12px;text-align:center;color:var(--muted);margin-top:8px}
/* blog */
.latest{position:absolute;top:606px;left:72px;font-family:Montserrat,Arial,sans-serif;font-weight:700;font-size:26px}
.posts{position:absolute;top:648px;left:72px;width:368px}
.post{height:284px}
.post .ph{height:168px}
.meta{margin-top:12px;text-align:center;font-size:9px;color:var(--orange)}
.post h3{margin-top:8px;text-align:center;font-size:12px;font-weight:700}
.post p{margin-top:8px;font-size:9px;line-height:13px;text-align:center;color:var(--muted);padding:0 24px}
/* sidebar */
.side{position:absolute;top:610px;left:472px;width:168px}
.author{background:var(--soft);height:210px;padding:12px;text-align:center}
.author .ph{height:126px}
.author h4{margin-top:14px;font-size:13px}
.author p{font-size:9px;color:var(--muted);margin-top:6px}
.more{margin-top:40px;background:var(--soft);padding:12px}
.more h4{text-align:center;font-size:12px;margin-bottom:12px}
.more .item .ph{height:96px}
.more .item p{font-size:8px;line-height:11px;color:var(--muted);margin:8px 0 14px}
.stuff{margin-top:30px;background:var(--orange);padding:14px;color:#fff}
.stuff h4{font-family:Montserrat,Arial,sans-serif;font-size:13px}
.stuff p{font-size:8px;line-height:11px;margin:8px 0}
.stuff .field{background:#fff;height:18px;margin-bottom:6px;font-size:8px;color:#999;padding:4px 6px}
.stuff .go{background:#222;color:#fff;font-size:8px;text-align:center;width:60px;margin:4px auto 0;padding:4px}
/* pagination */
.pager{position:absolute;top:2052px;left:72px;width:368px;display:flex;justify-content:center;gap:6px}
.pager span{width:18px;height:18px;border:1px solid #ccc;font-size:8px;display:flex;align-items:center;justify-content:center;color:var(--muted)}
.pager .on{background:var(--orange);border-color:var(--orange);color:#fff}
/* footer */
.connect{position:absolute;top:2112px;left:0;right:0;height:52px;background:var(--bar);display:flex;align-items:center;justify-content:center;gap:14px;color:#fff;font-weight:700;font-size:14px}
.connect i{width:14px;height:14px;border-radius:50%;background:#fff;display:block}
.footer{position:absolute;top:2164px;left:0;right:0;height:226px;background:var(--footer);color:#bbb}
.footer .brand{position:absolute;left:40px;top:30px}
.fcol{position:absolute;top:28px;font-size:8px;line-height:14px}
.fcol h5{color:#fff;font-size:11px;margin-bottom:6px}
.fcol .row{display:flex;align-items:center;gap:6px}
.fcol .row i{width:12px;height:12px;border-radius:50%;background:var(--orange);display:block}
.copy{position:absolute;bottom:14px;left:0;right:0;text-align:center;font-size:8px;color:#888}
</style>
</head>
<body>
<main class="page">
  <header class="hero" role="img" aria-label="Dark baking scene with wheat stalks, flour and grain bowls">
    <nav class="nav">
      <span class="active">Home</span><span>Tutorials</span><span>Bread Blog</span>
      <span class="brand"><span class="dot"></span>crumb42.com</span>
      <span>Recipes</span><span>Bread Blog</span><span>About</span>
      <svg class="search" viewBox="0 0 12 12"><circle cx="5" cy="5" r="3.5" fill="none" stroke="#fff" stroke-width="1.4"/><line x1="7.6" y1="7.6" x2="11" y2="11" stroke="#fff" stroke-width="1.4"/></svg>
      <span class="cta">Subscribe</span>
    </nav>
    <h1>Sed ut perspiciande<br>volup tatac cusantium</h1>
    <p>Ut enim ad minima veniam quis nostrum exercitationem ullam corporis suscipit laboriosam.</p>
    <span class="btn">Read More</span>
  </header>

  <section class="cats">
    <div class="cat"><div class="ph" role="img" aria-label="Loaves of fresh bread" style="background:linear-gradient(135deg,#c98a4b,#7a4a22)"></div><p>Neque porro quisquam est qui dolorem ipsum quia</p></div>
    <div class="cat"><div class="ph" role="img" aria-label="Sliced bread on a board" style="background:linear-gradient(135deg,#b9a58a,#5e4a34)"></div><p>Neque porro quisquam est qui dolorem ipsum quia</p></div>
    <div class="cat"><div class="ph" role="img" aria-label="Hands kneading dough" style="background:linear-gradient(135deg,#d8cfc4,#6e6256)"></div><p>Neque porro quisquam est qui dolorem ipsum quia</p></div>
    <div class="cat"><div class="ph" role="img" aria-label="Flour and grain in bowls" style="background:linear-gradient(135deg,#8c7a66,#2f261d)"></div><p>Neque porro quisquam est qui dolorem ipsum quia</p></div>
  </section>

  <h2 class="latest">Latest Blog</h2>
  <section class="posts">
    <article class="post"><div class="ph" role="img" aria-label="Baker shaping dough on a floured table" style="background:linear-gradient(135deg,#e2d6c6,#8a6f52)"></div><div class="meta">October 12, 2024 &nbsp; | &nbsp; 3 Comments</div><h3>At vero eosetaccusamusel iusto odio dignissimos</h3><p>Lorem ipsum dolor sit amet consectetur adipiscing elit sed do eiusmod tempor incididunt ut labore et dolore magna aliqua ut enim ad minim veniam quis nostrud.</p></article>
    <article class="post"><div class="ph" role="img" aria-label="Dough being rolled with flour dust" style="background:linear-gradient(135deg,#4a3a2c,#c8b8a2)"></div><div class="meta">October 12, 2024 &nbsp; | &nbsp; 3 Comments</div><h3>At vero eosetaccusamusel iusto odio dignissimos</h3><p>Lorem ipsum dolor sit amet consectetur adipiscing elit sed do eiusmod tempor incididunt ut labore et dolore magna aliqua ut enim ad minim veniam quis nostrud.</p></article>
    <article class="post"><div class="ph" role="img" aria-label="Baker in yellow apron kneading dough" style="background:linear-gradient(135deg,#f1e7d6,#e0a93a)"></div><div class="meta">October 12, 2024 &nbsp; | &nbsp; 3 Comments</div><h3>At vero eosetaccusamusel iusto odio dignissimos</h3><p>Lorem ipsum dolor sit amet consectetur adipiscing elit sed do eiusmod tempor incididunt ut labore et dolore magna aliqua ut enim ad minim veniam quis nostrud.</p></article>
    <article class="post"><div class="ph" role="img" aria-label="Bowls of grain and flour from above" style="background:linear-gradient(135deg,#a57a45,#e8dcc8)"></div><div class="meta">October 12, 2024 &nbsp; | &nbsp; 3 Comments</div><h3>At vero eosetaccusamusel iusto odio dignissimos</h3><p>Lorem ipsum dolor sit amet consectetur adipiscing elit sed do eiusmod tempor incididunt ut labore et dolore magna aliqua ut enim ad minim veniam quis nostrud.</p></article>
    <article class="post"><div class="ph" role="img" aria-label="Wheat ears beside a bowl of flour" style="background:linear-gradient(135deg,#d9c9b0,#6e5333)"></div><div class="meta">October 12, 2024 &nbsp; | &nbsp; 3 Comments</div><h3>At vero eosetaccusamusel iusto odio dignissimos</h3><p>Lorem ipsum dolor sit amet consectetur adipiscing elit sed do eiusmod tempor incididunt ut labore et dolore magna aliqua ut enim ad minim veniam quis nostrud.</p></article>
  </section>

  <aside class="side">
    <div class="author"><div class="ph" role="img" aria-label="Author portrait" style="background:linear-gradient(180deg,#cfc6bb,#8f8377)"></div><h4>Martin Hale</h4><p>Home baker and flour enthusiast</p></div>
    <div class="more">
      <h4>See More Posts</h4>
      <div class="item"><div class="ph" role="img" aria-label="Round sourdough loaf" style="background:linear-gradient(135deg,#6e4a2a,#2c1e14)"></div><p>October 12, 2024<br>Sed ut perspiciatis unde omnis iste natus</p></div>
      <div class="item"><div class="ph" role="img" aria-label="Dish with bread and herbs" style="background:linear-gradient(135deg,#b9a67c,#5d6a3a)"></div><p>October 12, 2024<br>Sed ut perspiciatis unde omnis iste natus</p></div>
      <div class="item"><div class="ph" role="img" aria-label="Bread rolls in a basket" style="background:linear-gradient(135deg,#c48a4e,#4b301b)"></div><p>October 12, 2024<br>Sed ut perspiciatis unde omnis iste natus</p></div>
    </div>
    <div class="stuff">
      <h4>Get more stuff</h4>
      <p>Subscribe for new recipes and baking tips delivered to your inbox.</p>
      <div class="field">Name</div>
      <div class="field">Email</div>
      <div class="go">Sign Up</div>
    </div>
  </aside>

  <div class="pager"><span class="on">1</span><span>2</span><span>3</span><span>4</span><span>5</span><span>&rsaquo;</span></div>

  <div class="connect">Conect With: <i></i><i></i><i></i></div>
  <footer class="footer">
    <div class="brand"><span class="dot"></span>crumb42.com</div>
    <div class="fcol" style="left:240px"><h5>Sitemap</h5>Home<br>Tutorials<br>Bread Blog<br>Recipes<br>About<br>Contact</div>
    <div class="fcol" style="left:380px"><h5>Archives</h5>June 2024<br>July 2024<br>August 2024<br>September 2024<br>October 2024</div>
    <div class="fcol" style="left:520px"><h5>Contact</h5>
      <div class="row"><i></i>hello@crumb42.com</div>
      <div class="row"><i></i>+1 555 014 2290</div>
      <div class="row"><i></i>12 Mill Lane, Ryefield</div>
    </div>
    <div class="copy">© 2024 crumb42.com All rights reserved | Privacy | Terms</div>
  </footer>
</main>
</body>
</html>
```